Retail Photo Calendar of Anchorage, Alaska

I am a professional photographer in Anchorage, Alaska. I'm looking for a designer to create a unique, pleasing design for a 12-month (24 pages plus front and back cover) 2016 RETAIL calendar using images of mine of the Anchorage, Alaska area. This is not a promotional calendar. This calendar will be sold to the public in retail stores. So it's more about the calendar & photos than my name. Design must be appealing to the average consumer. The designer would be responsible for completing the entire calendar project to give plate-ready files. We’ll need both the raw InDesign files with links, as well as a PDF to be printed as a proof and submitted to the printer.

Specs for the calendar are:
• one vertical photo on front cover
• back cover
• inside back cover pages x 2
• Grid page for each month
• 12 horizontal photos for the monthly pages based on these specifications:
o Size: 8 7/8” x 12”
o Pages: Front and Back Cover plus 24 pages

Attached are two sample designs, one I like (file name “sample inside good”) and one I don’t like (sample inside bad). The one I like and what I’d want for my calendar is;
• more elegant design than the bad design
• small photo inserted on the grid page
• Unique fonts
• Nice ghosted back design element (sun in this case—which matches the month of July in Alaska)
• A quote

The one I don’t like (bad) is:
• Too much like a block
• Fonts are not very elegant
• Not much in the way of design going on here

I will supply:
• Excell document with approximately 100 dates for holiday’s, moon phases and special days.
• High resolution files of the 13 main images and 12 smaller insets
• Copy for each month including; captions for photos, quotes etc.
• The actual dates for a 2016 calendar

In order for me to choose a designer, what I’m expecting for this initial design is for the designer to offer the following;

1. A design for the cover, using the vertical image of the dog team supplied - and this copy: Anchorage, Alaska & Vicinity 2016 Calendar Photography by Mark Halden

2. A design for ONE month on the inside--- ( 2 pages) photo placement, caption, calendar grid, design element, quote, small photo and previous/next month small grid. Do this using the one horizontal photo (airplanes) supplied – and greeking text for the potential copy of the photo caption, quote, etc.

A sample of what I'm looking for the designer to send me to choose their design is in the file labeled: "Cover and Inside Sample" --- the picture of an existing cover & inside of a calendar.

Once I choose the design and designer I prefer, he/she and I will then work together as I supply the rest of the images, dates and copy as mentioned above. Tweaks to be made as we go along. The deadline for the print-ready final, is to be completed by August 15, 2014 -- Once the final complete designs are made and confirmed to work for the printer is when I'll pay the designer the amount pledged.

PLEASE feel free to contact me before starting design work if I can help clarify what I am looking for here.

Target Market(s)

The general public living in or visiting Anchorage, Alaska

Industry/Entity Type

Printer

Font styles to use
Serif

Requirements
Must have
• elegant pleasing design

```html
<!DOCTYPE html>
<html lang="en">
<head>
<meta charset="utf-8">
<title>Anchorage, Alaska &amp; Vicinity 2016 — February</title>
<link href="https://fonts.googleapis.com/css2?family=Cinzel:wght@400&family=Cormorant+Garamond:wght@400;500&family=Great+Vibes&family=Raleway:wght@400;500&display=swap" rel="stylesheet">
<style>
  :root{
    --bg:#f1f1f1;
    --paper:#ffffff;
    --navy:#2f3752;
    --panel:#4d566f;
    --panel-edge:#6a7390;
    --panel-text:#e6e9f1;
    --year:#8da0d6;
    --teal:#4f8c91;
    --ink:#222222;
    --muted:#a8a8a8;
    --cell-edge:#d2d2d2;
    --ghost:#eef0f5;
    --photo-sky:#3d5f9c;
    --photo-hill:#2a3a1e;
    --photo-water:#3d4756;
  }
  *{margin:0;padding:0;box-sizing:border-box}
  html,body{width:882px;height:1200px;overflow:hidden;background:var(--bg)}
  body{position:relative;font-family:"Raleway",sans-serif;color:var(--ink)}

  .page{position:absolute;left:41px;top:8px;width:800px;height:1184px;background:var(--paper);box-shadow:0 2px 14px rgba(0,0,0,.12)}

  .hero-photo{position:absolute;left:20px;top:15px;width:754px;height:502px;
    background:linear-gradient(160deg,var(--photo-sky) 0%,#6b6e78 16%,var(--photo-hill) 30%,#3c4f24 52%,#474a44 64%,var(--photo-water) 78%,#2e3644 100%)}
  .rights{position:absolute;right:8px;bottom:6px;width:200px;font-family:Arial,sans-serif;font-size:5.4px;line-height:1.25;color:#fff;font-weight:bold}

  .caption{position:absolute;left:20px;top:524px;width:172px;font-size:7.2px;line-height:1.4;color:#444;text-align:justify}

  .holidays{position:absolute;left:392px;top:535px;font-size:7.2px;line-height:1.3;color:#555;list-style:none}
  .holidays b{display:inline-block;width:13px;text-align:right;margin-right:6px;color:var(--navy)}

  .byline{position:absolute;left:622px;top:532px;width:150px;text-align:center;color:var(--navy)}
  .byline .name{font-family:"Cormorant Garamond",serif;font-size:22px;font-weight:500;letter-spacing:.5px}
  .byline .sub{font-family:"Cinzel",serif;font-size:5px;letter-spacing:.4px;margin-top:1px}

  .fold-line{position:absolute;left:0;right:0;top:590px;border-top:1px solid #efefef}

  .month-title{position:absolute;right:20px;top:604px;font-family:"Cinzel",serif;font-size:50px;letter-spacing:1px;color:var(--navy);line-height:1}

  .weekdays{position:absolute;left:169px;top:674px;width:611px;display:grid;grid-template-columns:repeat(7,1fr);font-family:"Great Vibes",cursive;font-size:21px;color:var(--navy);text-align:center}
  .weekdays .weekend{color:var(--teal)}

  .ghost-mark{position:absolute;left:250px;top:880px;width:420px;text-align:center;color:var(--ghost);pointer-events:none}
  .ghost-mark .name{font-family:"Cormorant Garamond",serif;font-size:76px;line-height:1}
  .ghost-mark .sub{font-family:"Cinzel",serif;font-size:12px;margin-top:2px}

  .month-grid{position:absolute;left:169px;top:710px;width:611px;height:456px;display:grid;grid-template-columns:repeat(7,1fr);grid-template-rows:repeat(5,1fr);gap:7px 6px}
  .day{border-right:3px solid var(--cell-edge);border-bottom:3px solid var(--cell-edge);text-align:right;padding:1px 8px 0 0;font-family:"Cormorant Garamond",serif;font-size:19px;color:var(--ink)}
  .day.other{color:var(--muted)}

  .mini-cal{position:absolute;width:118px;font-family:"Cormorant Garamond",serif;font-size:10px;line-height:1.15}
  .mini-cal h3{font-family:"Cinzel",serif;font-weight:400;font-size:10px;text-align:right;letter-spacing:.3px}
  .mini-cal .grid{display:grid;grid-template-columns:repeat(7,1fr);text-align:center}
  .mini-cal .head{font-family:"Cinzel",serif;font-size:8.5px}
  .mini-cal .other{opacity:.45}
  .mini-cal.jan{left:18px;top:604px;color:var(--navy)}
  .mini-cal.mar{left:18px;top:1098px;color:var(--panel-text)}

  .side-note{position:absolute;left:18px;top:714px;width:120px;font-size:6.6px;line-height:1.35;color:#444;text-align:justify}
  .inset-photo{position:absolute;left:18px;top:774px;width:119px;height:79px;
    background:linear-gradient(165deg,#4d6a9e 0%,#2f4022 34%,#3e5030 55%,#3f4b5c 80%,#2c3543 100%)}

  .title-panel{position:absolute;left:18px;top:867px;width:118px;height:310px;background:var(--panel);border-left:3px solid var(--panel-edge);color:var(--panel-text);text-align:center}
  .title-panel .place{margin-top:34px;font-family:"Cinzel",serif;font-size:13.5px;line-height:1.05;letter-spacing:.4px}
  .title-panel .year{font-family:"Cormorant Garamond",serif;font-size:33px;line-height:1;color:var(--year);border-bottom:1px solid var(--panel-text);margin:0 8px;padding-bottom:1px}
  .title-panel .kind{font-family:"Cinzel",serif;font-size:4.5px;letter-spacing:.6px;margin-top:3px}
  .title-panel .credit{font-size:4.5px;letter-spacing:.6px;margin-top:20px;text-transform:uppercase}
  .title-panel .name{font-family:"Cormorant Garamond",serif;font-size:15px;margin-top:2px}
</style>
</head>
<body>
<main class="page">
  <div class="hero-photo" role="img" aria-label="Aerial photo: two small bush planes, one red and white and one yellow, flying over a fjord beside a forested mountainside with a coastal highway and snowy peaks">
    <p class="rights">All rights reserved. Copying, reproduction by any means and for any purpose is prohibited. Exceptions are cases when you have the express written permission of the author.</p>
  </div>

  <p class="caption">Lofty mountain peaks, ice-sculptured fjords, an abundance of marine wildlife and massive tidewater glaciers make the Top 10 list of things to see in Alaska and glacier cruises the best way to accomplish that.</p>

  <ul class="holidays">
    <li><b>2</b>Groundhog Day</li>
    <li><b>7</b>Big Game Sunday</li>
    <li><b>14</b>Valentines day</li>
    <li><b>15</b>Presidents day</li>
  </ul>

  <div class="byline">
    <div class="name">Mark Halden</div>
    <div class="sub">Anchorage, Alaska &amp; Vicinity - 2016</div>
  </div>

  <div class="fold-line"></div>

  <section class="mini-cal jan">
    <h3>January</h3>
    <div class="grid">
      <span class="head">S</span><span class="head">M</span><span class="head">T</span><span class="head">W</span><span class="head">T</span><span class="head">F</span><span class="head">S</span>
      <span class="other">27</span><span class="other">28</span><span class="other">29</span><span class="other">30</span><span class="other">31</span><span>1</span><span>2</span>
      <span>3</span><span>4</span><span>5</span><span>6</span><span>7</span><span>8</span><span>9</span>
      <span>10</span><span>11</span><span>12</span><span>13</span><span>14</span><span>15</span><span>16</span>
      <span>17</span><span>18</span><span>19</span><span>20</span><span>21</span><span>22</span><span>23</span>
      <span>24</span><span>25</span><span>26</span><span>27</span><span>28</span><span>29</span><span>30</span>
      <span>31</span><span class="other">1</span><span class="other">2</span><span class="other">3</span><span class="other">4</span><span class="other">5</span><span class="other">6</span>
    </div>
  </section>

  <p class="side-note">Lofty mountain peaks, ice-sculptured fjords, an abundance of marine wildlife and massive tidewater glaciers make the Top 10 list of things to see in Alaska and glacier cruises the best way to accomplish that.</p>

  <div class="inset-photo" role="img" aria-label="Small inset photo: bush planes over the fjord and mountains"></div>

  <aside class="title-panel">
    <div class="place">Anchorage,<br>Alaska<br>Vicinity</div>
    <div class="year">2016</div>
    <div class="kind">12 Month Calendar</div>
    <div class="credit">Photography by</div>
    <div class="name">Mark Halden</div>
  </aside>

  <section class="mini-cal mar">
    <h3>March</h3>
    <div class="grid">
      <span class="head">S</span><span class="head">M</span><span class="head">T</span><span class="head">W</span><span class="head">T</span><span class="head">F</span><span class="head">S</span>
      <span class="other">28</span><span class="other">29</span><span>1</span><span>2</span><span>3</span><span>4</span><span>5</span>
      <span>6</span><span>7</span><span>8</span><span>9</span><span>10</span><span>11</span><span>12</span>
      <span>13</span><span>14</span><span>15</span><span>16</span><span>17</span><span>18</span><span>19</span>
      <span>20</span><span>21</span><span>22</span><span>23</span><span>24</span><span>25</span><span>26</span>
      <span>27</span><span>28</span><span>29</span><span>30</span><span>31</span><span class="other">1</span><span class="other">2</span>
    </div>
  </section>

  <h1 class="month-title">February</h1>

  <div class="weekdays">
    <span class="weekend">Sunday</span><span>Monday</span><span>Tuesday</span><span>Wednesday</span><span>Thursday</span><span>Friday</span><span class="weekend">Saturday</span>
  </div>

  <div class="ghost-mark" aria-hidden="true">
    <div class="name">Mark Halden</div>
    <div class="sub">Anchorage &amp; Southcentral Alaska 2016</div>
  </div>

  <div class="month-grid">
    <div class="day other">31</div><div class="day">1</div><div class="day">2</div><div class="day">3</div><div class="day">4</div><div class="day">5</div><div class="day">6</div>
    <div class="day">7</div><div class="day">8</div><div class="day">9</div><div class="day">10</div><div class="day">11</div><div class="day">12</div><div class="day">13</div>
    <div class="day">14</div><div class="day">15</div><div class="day">16</div><div class="day">17</div><div class="day">18</div><div class="day">19</div><div class="day">20</div>
    <div class="day">21</div><div class="day">22</div><div class="day">23</div><div class="day">24</div><div class="day">25</div><div class="day">26</div><div class="day">27</div>
    <div class="day">28</div><div class="day">29</div><div class="day other">1</div><div class="day other">2</div><div class="day other">3</div><div class="day other">4</div><div class="day other">5</div>
  </div>
</main>
</body>
</html>
```